Logistics and freight company requires website

Hi, a logistic and freight company which is based in the United States needs an industry standard website for its activities. We are into forwarding and courier goods from within United States and Canada. We deliver a wide range of goods from shipping of electronics to document, clothings, etc. The proposed website should be comtemporary and youthful. I require brilliant colors for the website. The website should be the basic things of a site. There should a category for shipping electronics, clothings, documents and others( stuffs not listed within the three I mentioned).

```html
<!DOCTYPE html>
<html lang="en">
<head>
<meta charset="utf-8">
<title>Delivery &amp; Logistics</title>
<link rel="stylesheet" href="https://fonts.googleapis.com/css2?family=Open+Sans:wght@300;400;600;700;800&display=swap">
<style>
:root{
  --hero-blue:#1e4f9a;
  --blue:#1b6fd2;
  --cs-blue:#1c5aa8;
  --footer-blue:#1f8dcc;
  --yellow:#f7e51f;
  --title-blue:#2e7dd8;
  --card-frame:#eef0f3;
  --icon-grey:#7c8087;
  --text-grey:#555a60;
  --soft-white:#e6eefb;
  --white:#ffffff;
}
*{box-sizing:border-box;margin:0;padding:0}
html,body{width:1200px;height:2353px;overflow:hidden}
body{position:relative;font-family:"Open Sans",Arial,sans-serif;background:var(--white);color:var(--white)}
.abs{position:absolute}
.lines{white-space:nowrap}

/* hero */
.hero-bg{left:0;top:0;width:1200px;height:800px;background:linear-gradient(160deg,#2a5aa2 0%,#1c4d97 45%,#1a4589 100%)}
.hero-accent{left:0;top:0}
.logo{left:92px;top:44px;font-weight:800;font-size:28px;letter-spacing:.5px;color:var(--white);text-transform:uppercase}
.nav{top:60px;left:612px;list-style:none}
.nav li{position:absolute;font-size:14px;text-transform:uppercase;white-space:nowrap}
.nav .active::after{content:"";position:absolute;left:-12px;top:43px;width:70px;height:4px;background:var(--yellow)}
.hero-title{left:92px;top:262px;font-weight:800;font-size:80px;line-height:1.04;text-transform:uppercase}
.dash{width:26px;height:4px;background:var(--yellow)}
.hero-sub{left:92px;top:484px;font-size:20.5px;font-weight:300}
.btn{display:flex;align-items:center;justify-content:center;background:var(--yellow);color:#1b3c74;font-size:14px;font-weight:600;text-transform:uppercase;height:34px}
.courier-photo{left:540px;top:125px;width:600px;height:610px;border-radius:160px 160px 20px 20px;background:linear-gradient(180deg,#1d2c4d 0%,#223a6a 45%,#d8c3a2 75%,#e9e9ec 100%);opacity:.92}

/* who we are */
.who-title{left:0;width:1200px;top:786px;text-align:center;font-size:40px;font-weight:700;text-transform:uppercase}
.who-text{left:0;width:1200px;top:900px;text-align:center;font-size:16px;line-height:23.5px;letter-spacing:1.5px;font-weight:300;color:var(--soft-white)}
.call{left:0;width:1200px;top:1034px;text-align:center;font-size:38px;font-weight:800;color:var(--yellow);text-transform:uppercase}

/* shipping categories */
.card{top:1133px;width:306px;height:593px;border:8px solid var(--card-frame)}
.card-icon{position:absolute;left:50%;top:125px;transform:translateX(-50%)}
.card-title{position:absolute;left:0;width:100%;top:250px;text-align:center;font-size:24px;font-weight:700;color:var(--title-blue);text-transform:uppercase;white-space:nowrap}
.card .dash{position:absolute;left:50%;margin-left:-13px;top:302px}
.card-text{position:absolute;left:0;width:100%;top:338px;text-align:center;font-size:14.5px;line-height:21px;letter-spacing:1.4px;color:var(--text-grey)}
.card .btn{position:absolute;left:69px;top:492px;width:152px}

/* customer service */
.cs-bg{left:0;top:1824px;width:1200px;height:452px;background:radial-gradient(circle at 20% 70%,#2f7fd6 0%,var(--cs-blue) 45%,#1a4f95 100%)}
.agent-photo{left:157px;top:1757px;width:267px;height:519px;border-radius:120px 120px 0 0;background:linear-gradient(180deg,#4a2e22 0%,#6b4a3a 30%,#243d7a 60%,#1f3466 100%)}
.cs-title{left:554px;top:1888px;font-size:40px;font-weight:700;text-transform:uppercase}
.cs-text{left:554px;top:2012px;font-size:16px;line-height:23.5px;letter-spacing:1.5px;font-weight:300;color:var(--soft-white)}

/* footer */
.footer{left:0;top:2276px;width:1200px;height:77px;background:var(--footer-blue)}
.footer-nav li{position:absolute;top:2306px;font-size:13px;text-transform:uppercase;list-style:none}
.footer-logo{left:847px;top:2298px;font-weight:800;font-size:23px;color:var(--white);text-transform:uppercase}
</style>
</head>
<body>

<header>
  <div class="abs hero-bg" role="img" aria-label="Blurred blue photograph of a highway with moving traffic"></div>
  <svg class="abs hero-accent" width="1200" height="1240" viewBox="0 0 1200 1240" aria-hidden="true">
    <polygon points="533,337 1200,97 1200,690 643,740" fill="#f7e51f"/>
    <polygon points="0,784 1200,705 1200,1185 0,1232" fill="#1b6fd2"/>
    <polygon points="0,940 44,960 44,1122 0,1128" fill="#f7e51f"/>
  </svg>
  <div class="abs courier-photo" role="img" aria-label="Photo of a smiling courier in a navy cap and polo holding a parcel and a clipboard"></div>

  <div class="abs logo">Delivery &amp; Logistics</div>
  <ul class="abs nav">
    <li class="active" style="left:0">Home</li>
    <li style="left:90px">Services</li>
    <li style="left:198px">About</li>
    <li style="left:290px">News</li>
    <li style="left:374px">Contacts</li>
  </ul>

  <h1 class="abs hero-title">Fast Delivery<br>Service</h1>
  <div class="abs dash" style="left:94px;top:450px"></div>
  <p class="abs hero-sub">United States based delivery and logistics company</p>
  <a class="abs btn" style="left:93px;top:562px;width:152px">Make an order</a>
</header>

<section>
  <h2 class="abs who-title">Who we are</h2>
  <div class="abs dash" style="left:587px;top:856px"></div>
  <p class="abs who-text lines">So strongly and metaphysically did I conceive of my situation then, that while earnestly<br>watching his motions, I seemed distinctly to perceive that my own individuality was now<br>merged in a joint stock company of two; that my free will had received a mortal wound; and<br>that another's mistake or misfortune might plunge innocent me into unmerited disaster and</p>
  <p class="abs call">Call now: 1-800-555-0199</p>
</section>

<section>
  <article class="abs card" style="left:102px">
    <svg class="card-icon" width="86" height="80" viewBox="0 0 86 80" fill="none" stroke="#7c8087" stroke-width="2.5" stroke-linejoin="round" aria-hidden="true">
      <rect x="14" y="14" width="58" height="40" rx="2"/>
      <path d="M6 62h74l-6 8H12z"/>
      <path d="M36 66h14"/>
    </svg>
    <h3 class="card-title">Electronics</h3>
    <div class="dash"></div>
    <p class="card-text lines">So strongly and<br>metaphysically did I conceive<br>of my situation then, that<br>while earnestly watching his<br>motions, I seemed distinctly</p>
    <a class="btn">Read more</a>
  </article>

  <article class="abs card" style="left:449px">
    <svg class="card-icon" width="86" height="80" viewBox="0 0 86 80" fill="none" stroke="#7c8087" stroke-width="2.5" stroke-linejoin="round" aria-hidden="true">
      <path d="M32 8l-22 10 8 16 8-4v42h34V30l8 4 8-16-22-10c-2 6-6 9-11 9s-9-3-11-9z"/>
    </svg>
    <h3 class="card-title">Clothing</h3>
    <div class="dash"></div>
    <p class="card-text lines">So strongly and<br>metaphysically did I conceive<br>of my situation then, that<br>while earnestly watching his<br>motions, I seemed distinctly</p>
    <a class="btn">Read more</a>
  </article>

  <article class="abs card" style="left:795px">
    <svg class="card-icon" width="86" height="80" viewBox="0 0 86 80" fill="none" stroke="#7c8087" stroke-width="2.5" stroke-linejoin="round" stroke-linecap="round" aria-hidden="true">
      <path d="M22 6h30l14 14v54H22z"/>
      <path d="M52 6v14h14"/>
      <path d="M31 36h26M31 46h26M31 56h18"/>
    </svg>
    <h3 class="card-title">Documents &amp; Others</h3>
    <div class="dash"></div>
    <p class="card-text lines">So strongly and<br>metaphysically did I conceive<br>of my situation then, that<br>while earnestly watching his<br>motions, I seemed distinctly</p>
    <a class="btn">Read more</a>
  </article>
</section>

<section>
  <div class="abs cs-bg"></div>
  <div class="abs agent-photo" role="img" aria-label="Photo of a smiling customer service agent wearing a headset"></div>
  <h2 class="abs cs-title">24/7 Customer service</h2>
  <div class="abs dash" style="left:556px;top:1958px"></div>
  <p class="abs cs-text lines">So strongly and metaphysically did I conceive of my<br>situation then, that while earnestly watching his<br>motions, I seemed distinctly to perceive that my own<br>individuality was now merged in a joint stock company</p>
  <a class="abs btn" style="left:554px;top:2143px;width:152px">Online chat</a>
</section>

<footer>
  <div class="abs footer"></div>
  <ul class="footer-nav">
    <li style="left:78px">Home</li>
    <li style="left:163px">Services</li>
    <li style="left:262px">About</li>
    <li style="left:348px">News</li>
    <li style="left:430px">Contacts</li>
  </ul>
  <div class="abs footer-logo">Delivery &amp; Logistics</div>
</footer>

</body>
</html>
```